CuraNex System Web Page Design

This project is to design 6 pages of a web based medical system for clinics, hospitals, drugs suppliers, general items suppliers, insurance company, laboratories and patients (basically all parties which could be involved in).We want the designs of the browser, button, icon and layout are based on Vex, which is user friendly, looks professional, simple and neat but with powerful functions. We have uploaded few pictures of another system, please do not copy its design because this is not what we are looking for, the pictures are for you to know the elements should be included in our pages. CuraNex web-base system, design 6 pages1. Login PageShould include the following elements-company id with input field-login id with input field-password with input field2. Main Page (Navigation page)Should include the following elements-Appointment-Consultation-Patient-Drugs inventory -General supplies inventory -Laboratory-Suppliers-Insurance-Reports 3. Appointment PageShould include all the the elements in the respective pictures plus the followings-Daily View, Weekly View, Monthly View buttons4. Consultation PageShould include all the the elements in the respective picture5. Patient Page5.1 General information Should include all the the elements in the respective picture5.2 medical history/lab reportsShould include all the the elements in the respective picture plus the followings-Notify patient button-Share report button.
Updated on 28 Nov:
Please stop using Ward Keystone in your designs which is not the name of our system. We have just rename our system to CuraNex, please take note.
We need the system to look professional not playful, do not use too many colors and playful icons.
professional users

```html
<!DOCTYPE html>
<html lang="en">
<head>
<meta charset="UTF-8">
<title>CuraNex – Log In</title>
<link rel="stylesheet" href="https://fonts.googleapis.com/css2?family=Carlito:ital,wght@0,400;0,700;1,400&display=swap">
<style>
  :root {
    --brand-blue: #1c5fac;
    --field-bg: #ffffff;
    --field-border: #c9ccd1;
    --placeholder: #b4b8bd;
    --button-text: #1c5fac;
    --link-text: #ffffff;
    --logo-text: #ffffff;
  }
  * { box-sizing: border-box; margin: 0; padding: 0; }
  html, body {
    width: 1200px;
    height: 813px;
    overflow: hidden;
  }
  body {
    background: var(--brand-blue);
    font-family: "Carlito", "Calibri", sans-serif;
    position: relative;
  }
  .brand {
    position: absolute;
    top: 236px;
    left: 0;
    width: 1200px;
    text-align: center;
    color: var(--logo-text);
    font-weight: 700;
    font-size: 48px;
    line-height: 56px;
    letter-spacing: 0.5px;
  }
  .login-form {
    position: absolute;
    left: 450px;
    top: 355px;
    width: 300px;
  }
  .field {
    display: block;
    width: 300px;
    height: 37px;
    background: var(--field-bg);
    border: 1px solid var(--field-border);
    border-radius: 4px;
    padding: 0 22px;
    font-family: inherit;
    font-size: 14.5px;
    color: #333;
    outline: none;
  }
  .field::placeholder { color: var(--placeholder); }
  .field + .field { margin-top: 16px; }
  .field--password { margin-top: 16px; }
  .login-button {
    display: block;
    width: 300px;
    height: 38px;
    margin-top: 24px;
    background: var(--field-bg);
    border: none;
    border-radius: 5px;
    font-family: inherit;
    font-size: 15px;
    color: var(--button-text);
    cursor: pointer;
  }
  .forgot-link {
    display: block;
    margin-top: 14px;
    text-align: center;
    font-size: 12px;
    font-style: italic;
    color: var(--link-text);
    text-decoration: underline;
  }
</style>
</head>
<body>
  <div class="brand">CuraNex</div>

  <form class="login-form" action="#">
    <input class="field" type="text" placeholder="Company ID" aria-label="Company ID">
    <input class="field" type="text" placeholder="Login ID" aria-label="Login ID">
    <input class="field" type="password" placeholder="Password" aria-label="Password">
    <button class="login-button" type="button">Log In</button>
    <a class="forgot-link" href="#">Forget Password ?</a>
  </form>
</body>
</html>
```